Bravik = Difficult

Sto Je Treba Ni Bravik
what must be done, is not difficult...

my mom is Croatian and her name is Marela.

a Croatian expression that I came across 12 years ago is 'what must be done, is not difficult'. yes, it is counter-intuitive. but it helped me to get divorced and then to beat Stage 4 cancer. both seem impossible,

but they they had to be done, so they were not difficult.

so I have started up a new company called:
Bravik Consulting - solving difficult

I'll be working with companies that have a difficult program/project that they haven't launched yet...

I envision possibly a business card that is shaped into a "D" to represent the Croatian word of difficult.

yes, I know this is difficult - welcome to my new world - the difficult challenges are worth solving...

a nod to the red/white design of the Croatian flag would be nice.

```html
<!DOCTYPE html>
<html lang="en">
<head>
<meta charset="utf-8">
<title>Bravik Consulting – Business Card</title>
<link rel="stylesheet" href="https://fonts.googleapis.com/css2?family=Baloo+2:wght@700;800&family=Quicksand:wght@400&display=swap">
<style>
  :root {
    --brand-red: #e30613;
    --ink: #111111;
    --paper: #ffffff;
  }
  html, body {
    margin: 0;
    padding: 0;
    width: 1200px;
    height: 819px;
    overflow: hidden;
    background: var(--paper);
  }
  .card-sheet {
    display: block;
    width: 1200px;
    height: 819px;
  }
  .front-shape { fill: var(--brand-red); }
  .front-wordmark {
    font-family: "Baloo 2", sans-serif;
    font-weight: 800;
    font-size: 54px;
    fill: var(--paper);
  }
  .back-outline {
    fill: var(--paper);
    stroke: var(--brand-red);
    stroke-width: 2;
  }
  .back-band { fill: var(--brand-red); }
  .back-wordmark {
    font-family: "Baloo 2", sans-serif;
    font-weight: 800;
    font-size: 39px;
    fill: var(--brand-red);
  }
  .back-tagline {
    font-family: "Baloo 2", sans-serif;
    font-weight: 700;
    font-size: 27px;
    fill: var(--brand-red);
  }
  .contact-line {
    font-family: "Baloo 2", sans-serif;
    font-weight: 800;
    font-size: 19px;
    fill: var(--ink);
  }
  .contact-email {
    font-family: "Baloo 2", sans-serif;
    font-weight: 800;
    font-size: 15px;
    fill: var(--ink);
  }
  .motto {
    font-family: "Quicksand", sans-serif;
    font-weight: 400;
    font-size: 16px;
    fill: var(--ink);
  }
</style>
</head>
<body>
<svg class="card-sheet" viewBox="0 0 960 655" xmlns="http://www.w3.org/2000/svg">
  <defs>
    <clipPath id="back-clip">
      <path d="M550,73 H624 Q637,73 637,90 L640,232 C646,208 668,194 705,194 C805,194 882,272 882,372 C882,478 838,548 760,548 H580 Q565,548 564,532 L533,96 Q533,73 550,73 Z"/>
    </clipPath>
  </defs>

  <!-- Front: letter d -->
  <g class="card-front">
    <g role="img" aria-label="Red letter d filled with a white maze-like line pattern">
      <ellipse class="front-shape" cx="225" cy="368" rx="131" ry="182"/>
      <path class="front-shape" d="M340,72 H402 Q440,72 440,112 V530 Q440,548 420,548 H330 Q306,548 306,522 V110 Q306,72 340,72 Z"/>
    </g>
    <text class="front-wordmark" text-anchor="middle" transform="translate(208,318) rotate(-40)">Bravik</text>
    <text class="front-wordmark" text-anchor="middle" transform="translate(276,368) rotate(-40)">consulting</text>
  </g>

  <!-- Back: letter b -->
  <g class="card-back">
    <path class="back-outline" d="M550,73 H624 Q637,73 637,90 L640,232 C646,208 668,194 705,194 C805,194 882,272 882,372 C882,478 838,548 760,548 H580 Q565,548 564,532 L533,96 Q533,73 550,73 Z"/>
    <g clip-path="url(#back-clip)">
      <path class="back-band" role="img" aria-label="Red band with white chevron stripe pattern" d="M560,520 L880,410 L900,410 V560 H555 Z"/>
    </g>

    <text class="back-wordmark" text-anchor="end" transform="translate(598,118) rotate(-90)">Bravik Consulting</text>
    <text class="back-tagline" text-anchor="end" transform="translate(623,118) rotate(-90)">solving difficult</text>

    <g class="contact-block">
      <text class="contact-line" x="652" y="271">Dan Harlow</text>
      <text class="contact-line" x="652" y="296">418 Corbin Street</text>
      <text class="contact-line" x="652" y="321">Ellisburg, GA 30041</text>
      <text class="contact-line" x="652" y="346">Tel: 404-555-0193</text>
      <text class="contact-email" x="652" y="381">dan@bravikconsulting.com</text>
      <text class="motto" x="652" y="416">“What must be done,</text>
      <text class="motto" x="652" y="438">is not difficult”.</text>
    </g>
  </g>
</svg>
</body>
</html>
```